Waterjet manufacturing company needs brochure design

We need a brochure that outlines why waterjet manufacturing is beneficial for a variety of industries, our capabilities, core competencies and competitive advantages (see attached documents). The design should include our logo and include the same colours. (Dark blue RGB – 2,86,162, Light Blue RGB – 0,146,201). The design should be very clean, professional and eye catching. I've attached a few photos that can be used. Regarding the photo of the robot, please make the background white.
Updates

Target Market(s)

Manufacturing, construction, aerospace, home building

Colors

Designer to choose colors to be used in the design.

Requirements
Must have
• - exact Logo colours included in design (see description)
• - booklet style design (not tri-fold)
• - professional looking
• - Logo on front cover with writing underneath:
• High Quality
• Tight Tolerance
• Components
• - Chatterly, Workloop, Vidmora and Pixelane icons in Contact Us section

```html
<!DOCTYPE html>
<html lang="en">
<head>
<meta charset="utf-8">
<title>Ridgeline Waterjet Brochure Cover</title>
<link rel="stylesheet" href="https://fonts.googleapis.com/css2?family=Montserrat:wght@400;600;700;800&display=swap">
<style>
  :root {
    --dark-blue: rgb(2, 86, 162);
    --light-blue: rgb(0, 146, 201);
    --navy: #1f4f8c;
    --paper: #ffffff;
    --backdrop: #e4e4e4;
    --steel-a: #6f7a80;
    --steel-b: #a9a28c;
    --steel-c: #c9cfd3;
  }
  html, body {
    margin: 0;
    width: 1200px;
    height: 899px;
    overflow: hidden;
    background: var(--backdrop);
    font-family: "Montserrat", sans-serif;
  }
  .brochure-cover {
    position: absolute;
    left: 320px;
    top: 70px;
    width: 560px;
    height: 760px;
    background: var(--paper);
    box-shadow: 0 6px 24px rgba(0,0,0,0.12);
    overflow: hidden;
  }
  .cover-art {
    position: absolute;
    inset: 0;
  }
  .brand {
    position: absolute;
    left: 48px;
    top: 92px;
  }
  .brand-name {
    display: flex;
    align-items: center;
    gap: 10px;
    font-weight: 700;
    font-size: 22px;
    letter-spacing: 1.5px;
    color: var(--dark-blue);
    text-transform: uppercase;
  }
  .brand-square {
    width: 16px;
    height: 16px;
    background: var(--light-blue);
  }
  .brand-tagline {
    margin-top: 8px;
    font-size: 9px;
    font-weight: 600;
    letter-spacing: 2px;
    color: var(--dark-blue);
    text-transform: uppercase;
  }
  .cover-footer {
    position: absolute;
    left: 48px;
    top: 580px;
    width: 460px;
    color: #fff;
  }
  .headline {
    margin: 0 0 16px;
    font-size: 19px;
    line-height: 1.2;
    font-weight: 800;
    text-transform: uppercase;
    letter-spacing: 0.5px;
  }
  .contact-list {
    list-style: none;
    margin: 0;
    padding: 0;
    font-size: 10px;
    line-height: 1.6;
    font-weight: 400;
    opacity: 0.92;
  }
  .contact-list .gap { margin-top: 8px; }
</style>
</head>
<body>
  <article class="brochure-cover">
    <svg class="cover-art" width="560" height="760" viewBox="0 0 560 760">
      <defs>
        <linearGradient id="photo-tones" x1="0" y1="0" x2="1" y2="1">
          <stop offset="0" stop-color="#c9cfd3"/>
          <stop offset="0.5" stop-color="#6f7a80"/>
          <stop offset="1" stop-color="#a9a28c"/>
        </linearGradient>
      </defs>
      <polygon class="cover-photo" role="img" aria-label="Photo of a waterjet nozzle cutting circular parts from a metal sheet with water spray"
               points="240,0 560,0 560,440 0,550 0,370" fill="url(#photo-tones)"/>
      <polygon class="accent-light" points="300,470 560,372 560,430" fill="var(--light-blue)"/>
      <polygon class="footer-band" points="0,545 560,430 560,760 0,760" fill="var(--navy)"/>
      <polygon class="footer-band-edge" points="0,545 560,430 560,445 0,560" fill="var(--dark-blue)"/>
    </svg>

    <header class="brand">
      <div class="brand-name"><span class="brand-square"></span>Ridgeline Waterjet</div>
      <div class="brand-tagline">High Quality · Tight Tolerance · Components</div>
    </header>

    <footer class="cover-footer">
      <h1 class="headline">We have the most<br>powerful waterjet<br>in the Niagara region.</h1>
      <ul class="contact-list">
        <li>(905) 555-0142</li>
        <li>info@ridgelinewaterjet.com</li>
        <li>www.ridgelinewaterjet.com</li>
        <li class="gap">212 Fallow Lane, Suite 3, Brookhaven,</li>
        <li>ON K9Z 4T1</li>
      </ul>
    </footer>
  </article>
</body>
</html>
```